Criação de Logo + Papelaria + Manual Básico para Arquitetura
" Somos uma empresa pequena, eu e a minha sócia Clarice, atendemos o cliente, fazemos o levantamento de medidas e necessidades do cliente, desenvolvemos o projeto desde o início em 3D colorido, depois o projeto executivo e acompanhamento de obras. Estamos presentes no processo do início ao fim. Buscamos sempre atender o cliente da melhor maneira possível, sempre estando a par de todo o projeto. "

```html
<!DOCTYPE html>
<html lang="pt-BR">
<head>
<meta charset="UTF-8">
<title>Estúdio Vale — Cartão de Visita</title>
<link rel="stylesheet" href="https://fonts.googleapis.com/css2?family=Raleway:wght@300;400;800&display=swap">
<style>
  :root {
    --page: #ececec;
    --rose: #e3aea7;
    --rose-deep: #d39a93;
    --rose-soft: #efc6c0;
    --ink: #3a3a3a;
    --ink-soft: #6b6b6b;
    --black: #1c1c1c;
    --white: #ffffff;
  }
  * { margin: 0; padding: 0; box-sizing: border-box; }
  html, body {
    width: 1200px; height: 1200px; overflow: hidden;
    background: var(--page);
    font-family: "Raleway", sans-serif;
  }
  .sheet {
    position: relative; width: 1200px; height: 1200px;
    display: flex; flex-direction: column; align-items: center;
    justify-content: center; gap: 60px;
  }
  .card {
    position: relative; width: 840px; height: 480px;
    border-radius: 28px; overflow: hidden;
    box-shadow: 0 6px 24px rgba(0,0,0,0.10);
  }

  /* Front */
  .card--front {
    background: linear-gradient(135deg, var(--rose-soft) 0%, var(--rose) 55%, var(--rose-deep) 100%);
    display: flex; align-items: center; justify-content: center;
  }
  .brand { display: flex; align-items: center; gap: 26px; }
  .brand__dot {
    border-radius: 50%; background: var(--white); flex: none;
  }
  .card--front .brand__dot { width: 110px; height: 110px; }
  .brand__name {
    font-weight: 300; color: var(--ink); letter-spacing: 0.06em; white-space: nowrap;
  }
  .card--front .brand__name { font-size: 64px; }

  /* Back */
  .card--back { background: var(--white); }
  .card--back .brand { position: absolute; left: 96px; top: 62px; gap: 18px; }
  .card--back .brand__dot { width: 66px; height: 66px; background: var(--rose); }
  .card--back .brand__name { font-size: 38px; color: var(--ink-soft); }
  .person {
    position: absolute; left: 96px; top: 168px;
    font-weight: 800; font-size: 24px; letter-spacing: 0.04em; color: var(--black);
  }
  .handle {
    position: absolute; left: 38px; top: 150px;
    display: flex; align-items: center; gap: 8px;
    transform: rotate(-90deg); transform-origin: left top;
    translate: 0 200px;
    font-size: 15px; color: var(--ink-soft); white-space: nowrap;
  }
  .handle__dot { width: 12px; height: 12px; border-radius: 50%; background: var(--rose); }
  .contacts {
    position: absolute; right: 64px; bottom: 92px;
    list-style: none; display: flex; flex-direction: column; gap: 12px;
    text-align: right;
  }
  .contacts__item {
    display: flex; align-items: center; justify-content: flex-end; gap: 12px;
    font-size: 17px; color: var(--ink-soft);
  }
  .contacts__item--gap { margin-top: 10px; }
  .contacts__icon { width: 18px; height: 18px; flex: none; }
  .edge-band {
    position: absolute; left: 0; bottom: 0; width: 300px; height: 46px;
    background: var(--black);
  }
  .edge-band::after {
    content: ""; position: absolute; right: -60px; top: 0;
    width: 60px; height: 46px; background: var(--rose);
  }
</style>
</head>
<body>
<main class="sheet">

  <section class="card card--front" aria-label="Frente do cartão">
    <div class="brand">
      <span class="brand__dot"></span>
      <span class="brand__name">ESTÚDIO VALE</span>
    </div>
  </section>

  <section class="card card--back" aria-label="Verso do cartão">
    <div class="brand">
      <span class="brand__dot"></span>
      <span class="brand__name">ESTÚDIO VALE</span>
    </div>
    <p class="person">RENATA CLARICE</p>
    <p class="handle"><span class="handle__dot"></span>@estudiovale</p>

    <ul class="contacts">
      <li class="contacts__item">R. das Acácias, nº 120, Campinas - SP
        <svg class="contacts__icon" viewBox="0 0 24 24"><path d="M12 2a7 7 0 0 0-7 7c0 5 7 13 7 13s7-8 7-13a7 7 0 0 0-7-7zm0 9.5A2.5 2.5 0 1 1 12 6.5a2.5 2.5 0 0 1 0 5z" fill="var(--rose)"/></svg>
      </li>
      <li class="contacts__item">CEP 13010-000
        <span class="contacts__icon"></span>
      </li>
      <li class="contacts__item contacts__item--gap">contato@estudiovale.com.br
        <svg class="contacts__icon" viewBox="0 0 24 24"><rect x="3" y="5" width="18" height="14" rx="2" fill="var(--rose)"/><path d="M3 7l9 6 9-6" fill="none" stroke="var(--white)" stroke-width="1.6"/></svg>
      </li>
      <li class="contacts__item">www.estudiovale.com.br
        <svg class="contacts__icon" viewBox="0 0 24 24"><circle cx="12" cy="12" r="9" fill="none" stroke="var(--rose)" stroke-width="2"/><path d="M3 12h18M12 3c3 3 3 15 0 18M12 3c-3 3-3 15 0 18" fill="none" stroke="var(--rose)" stroke-width="1.5"/></svg>
      </li>
      <li class="contacts__item contacts__item--gap">(19) 98765-4321
        <svg class="contacts__icon" viewBox="0 0 24 24"><path d="M6.6 10.8a15 15 0 0 0 6.6 6.6l2.2-2.2a1 1 0 0 1 1-.25 11 11 0 0 0 3.6.6 1 1 0 0 1 1 1V20a1 1 0 0 1-1 1A17 17 0 0 1 3 4a1 1 0 0 1 1-1h3.5a1 1 0 0 1 1 1c0 1.25.2 2.45.6 3.6a1 1 0 0 1-.25 1z" fill="var(--rose)"/></svg>
      </li>
      <li class="contacts__item">(19) 3234-5678
        <span class="contacts__icon"></span>
      </li>
    </ul>

    <div class="edge-band"></div>
  </section>

</main>
</body>
</html>
```